business card design for luxurious real estate brand

using the attached logo, i am looking for a 2-sided business card design. the back should be the gold logo on black background. the front needs to include: gold logo, name, phone, email, and website

Industry/Entity Type

real estate

Contact Information for Business Card

logo, name, email, phone, website

Font styles to use
Sans Serif

```html
<!DOCTYPE html>
<html lang="en">
<head>
<meta charset="UTF-8">
<title>Villa Crestmoor – Business Card</title>
<link rel="stylesheet" href="https://fonts.googleapis.com/css2?family=Source+Sans+3:wght@400;600;700&display=swap">
<style>
  :root {
    --backdrop: #e4e4e4;
    --card-dark: #2c2a29;
    --card-light: #f4f4f4;
    --gold: #d4a72c;
    --accent-yellow: #f2c31b;
    --ink: #2e2e2e;
  }
  * { margin: 0; padding: 0; box-sizing: border-box; }
  html, body {
    width: 1200px;
    height: 960px;
    overflow: hidden;
    background: var(--backdrop);
    font-family: "Source Sans 3", "Source Sans Pro", Arial, sans-serif;
  }
  .canvas { position: relative; width: 1200px; height: 960px; }

  .card {
    position: absolute;
    width: 612px;
    height: 350px;
  }
  .card-back {
    left: 293px;
    top: 118px;
    background: var(--card-dark);
    display: flex;
    align-items: center;
    justify-content: center;
  }
  .card-front {
    left: 296px;
    top: 507px;
    background: var(--card-light);
  }

  .brand-name {
    color: var(--gold);
    font-weight: 600;
    text-transform: uppercase;
    white-space: nowrap;
  }
  .card-back .brand-name {
    font-size: 30px;
    letter-spacing: 4px;
    margin-top: 10px;
  }
  .card-front .brand-name {
    position: absolute;
    left: 47px;
    top: 112px;
    font-size: 22px;
    letter-spacing: 3px;
  }

  .holder {
    position: absolute;
    right: 47px;
    top: 166px;
    text-align: right;
  }
  .holder-name {
    color: var(--accent-yellow);
    font-weight: 700;
    font-size: 19px;
    letter-spacing: 0.3px;
    text-transform: uppercase;
    line-height: 24px;
  }
  .holder-title {
    color: var(--ink);
    font-size: 15px;
    line-height: 20px;
    margin-top: 5px;
  }
  .divider {
    position: absolute;
    left: 47px;
    top: 205px;
    width: 380px;
    height: 1px;
    background: var(--accent-yellow);
  }

  .contact-list {
    position: absolute;
    left: 47px;
    top: 253px;
    list-style: none;
  }
  .contact-item {
    display: flex;
    align-items: center;
    gap: 6px;
    color: var(--ink);
    font-size: 15px;
    line-height: 20.5px;
  }
  .contact-icon {
    width: 13px;
    height: 13px;
    flex: none;
  }
</style>
</head>
<body>
<div class="canvas">

  <section class="card card-back" aria-label="Card back">
    <div class="brand-name">Villa Crestmoor</div>
  </section>

  <section class="card card-front" aria-label="Card front">
    <div class="brand-name">Villa Crestmoor</div>

    <div class="holder">
      <div class="holder-name">Daniel Harper</div>
      <div class="holder-title">Managing Director</div>
    </div>
    <div class="divider"></div>

    <ul class="contact-list">
      <li class="contact-item">
        <svg class="contact-icon" viewBox="0 0 16 16" aria-hidden="true">
          <path d="M3.5 1.5l2.5 3-1.5 1.8c.8 1.8 2.3 3.3 4.2 4.2l1.8-1.5 3 2.5-1.3 2.5C6.5 13.8 2.2 9.5 1 3z" fill="var(--accent-yellow)"/>
        </svg>
        <span>(555) 010-2468</span>
      </li>
      <li class="contact-item">
        <svg class="contact-icon" viewBox="0 0 16 16" aria-hidden="true">
          <rect x="1" y="3" width="14" height="10" fill="none" stroke="var(--accent-yellow)" stroke-width="1.8"/>
          <path d="M1.5 3.5L8 9l6.5-5.5" fill="none" stroke="var(--accent-yellow)" stroke-width="1.6"/>
        </svg>
        <span>daniel@villacrestmoor.com</span>
      </li>
      <li class="contact-item">
        <svg class="contact-icon" viewBox="0 0 16 16" aria-hidden="true">
          <circle cx="8" cy="8" r="6.5" fill="none" stroke="var(--accent-yellow)" stroke-width="1.5"/>
          <ellipse cx="8" cy="8" rx="2.8" ry="6.5" fill="none" stroke="var(--accent-yellow)" stroke-width="1.2"/>
          <path d="M1.5 8h13M2.5 5h11M2.5 11h11" stroke="var(--accent-yellow)" stroke-width="1.1"/>
        </svg>
        <span>www.villacrestmoor.com</span>
      </li>
    </ul>
  </section>

</div>
</body>
</html>
```